Pet Shop Website

website will need to have the following features:
• Photo Galleries of each species (Dogs, Cats, Birds, Fish, Reptiles, Rabbits) in a light box popup
o Each species may have several different categories for example:
 Fish
• Marine fish
• Fresh water
• tropical
• Cichlid
• Information Fact sheets of each species – Downloaded as a pdf which can be either
o Care Sheets
o Training Sheets
• Members Area
o Username (Email Address) & Password login
o New signups
o Exclusive Member Deals
o Newsletter options

The front page must be very simple (for example lumavest.com.au) contain the following:
• Product of the week - which can be purchased online
o Short details
o Cost
• Pet Club Sign up picture
• Animal of the week/month
• Contact Phone Number and addresses of the stores
• A jQuery slideshow (Images could include stores, pets etc…)
The main page MUST keep simple. We do not want it cluttered.

Inner Page
The animals / reptile page will need to have:
• Short description of the species
• Photo Galleries
• A list of what is in stock and the list needs to clearly be sorted by each store (Use of Tabs maybe).
• Facts sheets / Info sheets
The type of website ideas (not the type of look that we are necessary after) is and the sort of content that we want to offer are as follows:

http://www.scalenook.com.au/
http://www.brindlecovepaws.com.au/
http://www.thefurrowden.com.au
http://www.tailtown.net.au

Colour in the new website:
Blue
Red
Grey
Yellow

Original site:

http://www.critterglow.com.au
Updates

Hi Guys,

We had feedback from the client and they would like to see a few dark designs.

Thanks                                   

Reason: We would like to reopen this contest back up for a further week

Target Market(s)

Targeting animal lovers

Industry/Entity Type

Store

Requirements
Should not have
• Alter the logo in anyway

```html
<!DOCTYPE html>
<html lang="en">
<head>
<meta charset="utf-8">
<title>Critter Glow – Pet Superstores</title>
<link href="https://fonts.googleapis.com/css2?family=Ubuntu:wght@400;500;700&family=Arimo:ital,wght@0,400;0,700;1,700&family=Noto+Serif:wght@900&display=swap" rel="stylesheet">
<style>
:root{
  --navy:#0a1a7a;
  --navy-deep:#06105a;
  --yellow:#f2dc00;
  --red:#e0001b;
  --grey-text:#555;
  --body-text:#222;
  --heading-grey:#5a5a5a;
  --footer-bg:#e8e8e8;
  --card-line:#d6d6d6;
}
*{box-sizing:border-box;margin:0;padding:0}
html,body{width:1081px;height:1200px;overflow:hidden}
body{font-family:"Arimo",Arial,sans-serif;color:var(--body-text);background:#fff}
.page{position:relative;width:1081px;height:1200px;overflow:hidden;
  background:
    radial-gradient(ellipse 300px 200px at 250px 150px,rgba(240,190,220,.55),transparent 70%),
    radial-gradient(ellipse 420px 260px at 700px 260px,rgba(190,200,245,.6),transparent 70%),
    radial-gradient(ellipse 300px 220px at 980px 60px,rgba(150,180,240,.7),transparent 70%),
    radial-gradient(ellipse 380px 200px at 150px 40px,rgba(190,210,245,.6),transparent 70%),
    linear-gradient(#eef0fb 0,#f6f4fb 420px,#f7f7f7 540px,#fdfdfd 800px,#fff 1112px);}
.abs{position:absolute}
.brand{left:108px;top:30px;display:flex;align-items:center;gap:10px;font-family:"Ubuntu",sans-serif;font-weight:700;font-size:34px;color:var(--navy)}
.brand-dot{width:26px;height:26px;border-radius:50%;background:var(--yellow)}
.phone-icon{left:675px;top:45px}
.call{left:756px;top:61px;width:234px;height:38px;border-radius:19px;background:rgba(255,255,255,.85);
  font-family:"Ubuntu",sans-serif;font-weight:500;font-size:22px;color:var(--heading-grey);line-height:38px;text-align:center}
.nav{left:92px;top:114px;width:896px;height:41px;border-radius:21px;
  background:linear-gradient(#1e2f9e,var(--navy) 50%,var(--navy-deep));border:1px solid #fff;box-shadow:0 1px 3px rgba(0,0,0,.25)}
.nav-item{position:absolute;top:0;height:41px;line-height:41px;font-family:"Ubuntu",sans-serif;font-weight:700;font-size:11.5px;color:#fff;letter-spacing:.3px;transform:translateX(-50%)}
.nav-sep{position:absolute;top:4px;width:1px;height:33px;background:rgba(255,255,255,.25)}
.nav-home{left:133px;top:104px;width:96px;height:51px;background:linear-gradient(#f7e600,#e9cf00);
  font-family:"Ubuntu",sans-serif;font-weight:700;font-size:11.5px;color:var(--navy-deep);text-align:center;line-height:62px}
.search{left:783px;top:123px;width:192px;height:24px;border-radius:12px;background:#fff;font-size:11px;color:#555;line-height:24px;padding-left:12px}
.search svg{position:absolute;right:10px;top:4px}
.hero-welcome{left:101px;top:198px;font-family:"Ubuntu",sans-serif;font-weight:700;font-size:27px;color:var(--heading-grey)}
.hero-title{left:99px;top:230px;font-family:"Ubuntu",sans-serif;font-weight:700;font-size:40px;color:var(--red);letter-spacing:-.5px}
.hero-sub{left:101px;top:276px;font-family:"Ubuntu",sans-serif;font-weight:700;font-size:24px;color:#e8d200}
.hero-text{left:105px;top:319px;width:418px;font-size:11.5px;line-height:16.2px;color:#333}
.hero-steps{left:100px;top:398px}
.hero-art{left:567px;top:212px;width:437px;height:306px;border-radius:40% 40% 10px 10px;
  background:radial-gradient(ellipse at 40% 45%,#c98a5c 0,#d9b69c 35%,rgba(240,236,240,0) 72%)}
.hero-floor{left:0;top:536px;width:1081px;height:4px;background:linear-gradient(#e0e0e0,#f4f4f4)}
.slider-ctrl{left:439px;top:525px;width:162px;height:33px;border-radius:17px;background:linear-gradient(#fafafa,#e6e6e6);border:1px solid #d0d0d0}
.products{left:93px;top:584px;width:894px;height:176px;border-radius:10px;background:linear-gradient(#fff 30%,#e7e7e7);border:1px solid #e2e2e2;display:flex}
.product{position:relative;text-align:center;border-right:1px solid var(--card-line)}
.product:last-child{border-right:0}
.product-img{margin:12px auto 0;width:184px;height:97px;border-radius:8px;background:linear-gradient(#f4ece6,#d9b894 60%,#c9a27e)}
.product-name{margin-top:14px;font-size:11px;line-height:16px;color:#333;letter-spacing:.2px}
.product-price{margin-top:5px;font-size:11px;font-weight:700;color:var(--red)}
.kittens{left:99px;top:797px;width:279px;height:279px;border-radius:45% 45% 20% 20%;
  background:radial-gradient(ellipse at 50% 55%,#d99a5c 0,#c98d5a 35%,#b49a80 55%,rgba(255,255,255,0) 72%)}
.welcome-title{left:400px;top:808px;font-family:"Noto Serif",serif;font-weight:900;font-size:27px;color:var(--red)}
.welcome-sub{left:401px;top:843px;font-family:"Arimo",sans-serif;font-weight:700;font-size:16px;color:#9a9a9a}
.welcome-text{left:400px;width:221px;font-size:11.3px;line-height:16.2px;color:#333;text-align:justify}
.divider-v{left:643px;top:797px;height:315px;border-left:1px dotted #999}
.contact-title{left:662px;top:806px;font-family:"Ubuntu",sans-serif;font-weight:500;font-size:22px;color:#333}
.store{left:662px;font-size:11.3px;line-height:16.2px;color:#222}
.store-name{font-weight:700;font-style:italic;color:var(--red)}
.dog-art{left:864px;top:837px;width:112px;height:166px;border-radius:45% 45% 30% 30%;background:linear-gradient(#c9985e,#d7ae7a 55%,#e8d2b3)}
.divider-h{left:657px;top:1015px;width:302px;border-top:1px solid #bbb}
.follow{left:667px;top:1030px;font-family:"Ubuntu",sans-serif;font-weight:500;font-size:15.5px;color:#333}
.social{top:1060px;width:43px;height:43px;border-radius:50%;background:radial-gradient(circle at 40% 35%,#5aa7e6,#1a5fb0);border:2px solid #e3e8f0}
.footer{left:0;top:1113px;width:1081px;height:87px;background:var(--footer-bg);text-align:center;font-size:11.3px;color:#222}
.footer-links{padding-top:28px;word-spacing:2px}
.footer-links span{margin:0 12px;color:#444}
.footer-legal{margin-top:5px}
</style>
</head>
<body>
<div class="page">

  <div class="abs brand"><span class="brand-dot"></span>Critter Glow</div>

  <svg class="abs phone-icon" width="72" height="60" viewBox="0 0 72 60" aria-hidden="true">
    <circle cx="16" cy="22" r="8" fill="#cfe3f7"/><circle cx="56" cy="22" r="8" fill="#cfe3f7"/>
    <ellipse cx="16" cy="42" rx="14" ry="9" fill="#cfe3f7"/><ellipse cx="56" cy="42" rx="14" ry="9" fill="#cfe3f7"/>
    <circle cx="36" cy="12" r="10" fill="#2a8fd8"/>
    <ellipse cx="36" cy="38" rx="18" ry="16" fill="#2a8fd8"/>
    <circle cx="36" cy="44" r="11" fill="#fff"/>
    <path d="M31 39c1 5 4 8 9 10l2-2-3-2-2 1c-2-1-3-3-4-5l1-2-2-3z" fill="#2a8fd8"/>
  </svg>
  <div class="abs call">Call : (08) 5550 1800</div>

  <nav class="abs nav">
    <span class="nav-sep" style="left:166px"></span>
    <span class="nav-sep" style="left:289px"></span>
    <span class="nav-sep" style="left:406px"></span>
    <span class="nav-item" style="left:215px">ABOUT US</span>
    <span class="nav-item" style="left:341px">PETS</span>
    <span class="nav-item" style="left:480px">CONTACT US</span>
  </nav>
  <div class="abs nav-home">HOME PAGE</div>
  <div class="abs search">-------Search here-----------
    <svg width="17" height="17" viewBox="0 0 17 17" aria-hidden="true"><circle cx="7" cy="7" r="5" fill="none" stroke="#333" stroke-width="2.2"/><path d="M11 11l5 5" stroke="#333" stroke-width="2.8" stroke-linecap="round"/></svg>
  </div>

  <div class="abs hero-welcome">Welcome to Critter Glow</div>
  <div class="abs hero-title">YOUR PET SUPERSTORES</div>
  <div class="abs hero-sub">at Harbourvale and Reedmere</div>
  <p class="abs hero-text">Lorem Ipsum is simply dummy text of the printing and typesetting industry. Lorem Ipsum has been the industry's standard dummy text ever since the 1500s,printing and typesetting industry. Lorem Ipsum has been the industry's standard dummy text ever since the 1500s,</p>

  <svg class="abs hero-steps" width="230" height="100" viewBox="0 0 230 100" aria-hidden="true" font-family="Times New Roman,serif" font-size="34" fill="#222">
    <path d="M4 40a41 41 0 0 0 80 22" fill="none" stroke="#e8192c" stroke-width="3"/>
    <path d="M84 40a41 41 0 0 1 64-38" fill="none" stroke="#ccc" stroke-width="3"/>
    <path d="M145 28a41 41 0 0 1 74 58" fill="none" stroke="#bbb" stroke-width="3"/>
    <text x="34" y="58">1</text><text x="110" y="56">2</text><text x="175" y="71">3</text>
  </svg>

  <div class="abs hero-art" role="img" aria-label="Group of pets: a large dog, a terrier, a parrot, frogs, a fishbowl, a canary, a guinea pig and a lizard"></div>

  <div class="abs hero-floor"></div>
  <svg class="abs slider-ctrl" width="162" height="33" viewBox="0 0 162 33" aria-hidden="true">
    <circle cx="23" cy="16" r="9" fill="#fff" stroke="#999"/><path d="M25 12l-4 4 4 4z" fill="#555"/>
    <circle cx="43" cy="16" r="5" fill="#888"/>
    <circle cx="61" cy="16" r="5" fill="#ccc"/><circle cx="79" cy="16" r="5" fill="#ccc"/>
    <circle cx="97" cy="16" r="5" fill="#ccc"/><circle cx="115" cy="16" r="5" fill="#ccc"/>
    <circle cx="137" cy="16" r="9" fill="#fff" stroke="#999"/><path d="M135 12l4 4-4 4z" fill="#555"/>
  </svg>

  <section class="abs products">
    <div class="product" style="width:222px">
      <div class="product-img" role="img" aria-label="Puppies and a kitten sitting together"></div>
      <p class="product-name">No extended hours over the Christmas<br>Period Fish Tank Setup</p>
      <p class="product-price">$1,097.00 AUD</p>
    </div>
    <div class="product" style="width:228px">
      <div class="product-img" role="img" aria-label="Puppy in a festive hat beside gift boxes"></div>
      <p class="product-name">No extended hours over the Christmas<br>Period Fish Tank Setup</p>
      <p class="product-price">$1,097.00 AUD</p>
    </div>
    <div class="product" style="width:220px">
      <div class="product-img" role="img" aria-label="Cats and a dog beside food bowls"></div>
      <p class="product-name">No extended hours over the Christmas<br>Period Fish Tank Setup</p>
      <p class="product-price">$1,097.00 AUD</p>
    </div>
    <div class="product" style="width:224px">
      <div class="product-img" role="img" aria-label="Puppy in a festive hat beside gift boxes"></div>
      <p class="product-name">No extended hours over the Christmas<br>Period Fish Tank Setup</p>
      <p class="product-price">$1,097.00 AUD</p>
    </div>
  </section>

  <div class="abs kittens" role="img" aria-label="Two kittens, a tabby and a ginger, sitting side by side"></div>

  <h2 class="abs welcome-title">WELCOME!</h2>
  <h3 class="abs welcome-sub">To Our Website</h3>
  <p class="abs welcome-text" style="top:875px">Praesent vestibulum molestie lacus. Aeneanum nonummy hendrerit mauris. Phasellus portame. Fusce suscipit varius mium sociis natoquemetun penatibus et magnis dis parturient.</p>
  <p class="abs welcome-text" style="top:1006px">Montes, nascetur ridiculus mus. Nulla dui. Fusce feugiat malesuada odio morbi nunc odio gravida atem cursus nluctus lorem maecenas tristique.</p>

  <div class="abs divider-v"></div>

  <h2 class="abs contact-title">Contact Information</h2>
  <address class="abs store" style="top:846px;font-style:normal">
    <span class="store-name">Shop 8 / 1500 Coralind Hwy</span><br>
    HARBOURVALE W.A 6999<br>Phone: (08) 5550 1970<br>Fax: (08) 5550 1960
  </address>
  <address class="abs store" style="top:929px;font-style:normal">
    <span class="store-name">Unit 1 / 10 Lantern Drive</span><br>
    REEDMERE W.A 6998<br>Phone: (08) 5550 6619<br>Fax: (08) 5550 6613
  </address>
  <div class="abs dog-art" role="img" aria-label="Seated dog holding a contact sign"></div>

  <div class="abs divider-h"></div>
  <div class="abs follow">Follow Us On:</div>
  <span class="abs social" style="left:660px" role="img" aria-label="Social network one"></span>
  <span class="abs social" style="left:717px" role="img" aria-label="Social network two"></span>
  <span class="abs social" style="left:775px" role="img" aria-label="Social network three"></span>

  <footer class="abs footer">
    <p class="footer-links">Home<span>|</span>About Us<span>|</span>Health<span>|</span>Body<span>|</span>Skin<span>|</span>Beauty<span>|</span>Contact Us</p>
    <p class="footer-legal">Lumavest &nbsp;&nbsp; Copyright 2011. &nbsp; Privacy Policy &nbsp;| &nbsp;Terms of Use</p>
  </footer>

</div>
</body>
</html>
```